Tufted Hollow is company name.Handknit&crochet blankets&scarves. Need logo&business ...

I need a design that is eye catching, using yarn and is flowing. I'd like to see colors in aqua (Larkin Peabody paint LP9043 Aquastone) for the yarn and company name. For the text, a dark grey color (Larkin Peabody LP7622 Hamburg Gray)

Colors
87cfc7

```html
<!DOCTYPE html>
<html lang="en">
<head>
<meta charset="utf-8">
<title>Tufted Hollow – Business Card</title>
<link rel="stylesheet" href="https://fonts.googleapis.com/css2?family=Delius&display=swap">
<style>
  :root {
    --page-bg: #f4f2ee;
    --card-bg: #eee2c6;
    --card-edge: #e2d3b2;
    --text-grey: #4f5556;
    --brand-blue: #7d96cc;
    --cable-light: #f6ecd6;
    --cable-shade: #d9c8a4;
    --flower-aqua: #5fb0c4;
    --flower-orange: #e98a45;
    --flower-lilac: #9d9ad6;
    --flower-green: #a9c98c;
    --flower-pink: #e07f86;
  }
  * { box-sizing: border-box; margin: 0; padding: 0; }
  html, body { width: 1200px; height: 1200px; overflow: hidden; }
  body {
    background: var(--page-bg);
    font-family: "Delius", sans-serif;
    color: var(--text-grey);
    position: relative;
  }
  .card {
    position: absolute;
    top: 185px;
    width: 500px;
    height: 830px;
    background: var(--card-bg);
    border: 1px solid var(--card-edge);
    border-radius: 22px;
    overflow: hidden;
    box-shadow: 0 6px 18px rgba(0,0,0,0.12);
  }
  .card--back { left: 70px; }
  .card--front { left: 630px; }

  .decor { position: absolute; }
  .decor--cable-top {
    top: 0; left: 0; width: 100%; height: 150px;
    background: linear-gradient(180deg, var(--cable-shade) 0%, var(--cable-light) 55%, var(--card-bg) 100%);
    opacity: 0.75;
  }
  .decor--cable-bottom {
    bottom: 0; left: 0; width: 100%; height: 160px;
    background: linear-gradient(0deg, var(--cable-shade) 0%, var(--cable-light) 55%, var(--card-bg) 100%);
    opacity: 0.75;
  }
  .decor--flower-aqua {
    top: 10px; right: 110px; width: 120px; height: 115px; border-radius: 50%;
    background: radial-gradient(circle, #4a5663 0 22%, var(--flower-aqua) 24% 100%);
  }
  .decor--flower-cluster {
    top: 0; right: 0; width: 210px; height: 250px;
    border-bottom-left-radius: 120px;
    background: radial-gradient(circle at 40% 25%, var(--flower-green) 0 25%, transparent 26%),
                radial-gradient(circle at 75% 30%, var(--flower-orange) 0 30%, transparent 31%),
                radial-gradient(circle at 60% 70%, var(--flower-lilac) 0 28%, transparent 29%),
                linear-gradient(200deg, var(--cable-light), var(--card-bg));
  }
  .decor--cable-corner {
    bottom: 0; left: 0; width: 170px; height: 230px;
    border-top-right-radius: 90px;
    background: radial-gradient(circle at 30% 25%, var(--flower-pink) 0 26%, transparent 27%),
                linear-gradient(0deg, var(--cable-shade), var(--cable-light));
  }

  .care { position: absolute; top: 330px; left: 70px; right: 30px; }
  .care__title { font-size: 30px; letter-spacing: 0.5px; margin-bottom: 14px; }
  .care__list { list-style: none; font-size: 27px; line-height: 1.25; }
  .care__list li { position: relative; padding-left: 34px; }
  .care__list li::before {
    content: ""; position: absolute; left: 4px; top: 0.5em;
    width: 12px; height: 12px; border-radius: 50%; background: var(--text-grey);
  }

  .brand {
    position: absolute; top: 95px; left: 40px;
    display: flex; align-items: center; gap: 14px;
  }
  .brand__mark { width: 40px; height: 40px; border-radius: 50%; background: var(--brand-blue); }
  .brand__name { font-size: 54px; line-height: 1.05; color: var(--brand-blue); }

  .contact { position: absolute; top: 345px; right: 40px; text-align: right; }
  .contact__name { font-size: 44px; margin-bottom: 22px; }
  .contact__phone { font-size: 20px; margin-bottom: 4px; }
  .contact__email-line { font-size: 20px; }
  .contact__email {
    position: absolute; top: 520px; left: 22px; right: 22px;
    font-size: 20px; white-space: nowrap;
  }
  .services {
    position: absolute; top: 590px; right: 40px; text-align: right;
    font-size: 24px; line-height: 1.12;
  }
</style>
</head>
<body>
  <section class="card card--back">
    <div class="decor decor--cable-top" role="img" aria-label="Cream cable-knit rope braid border"></div>
    <div class="decor decor--flower-aqua" role="img" aria-label="Aqua crocheted yarn flower with a button centre"></div>
    <div class="care">
      <h2 class="care__title">CARE INSTRUCTIONS:</h2>
      <ul class="care__list">
        <li>Machine wash cold, delicate cycle.</li>
        <li>Lay flat to dry.</li>
        <li>Do not dry clean.</li>
        <li>Do not iron.</li>
        <li>No bleach.</li>
      </ul>
    </div>
    <div class="decor decor--cable-bottom" role="img" aria-label="Cream cable-knit rope braid border"></div>
  </section>

  <section class="card card--front">
    <div class="decor decor--flower-cluster" role="img" aria-label="Cluster of knitted heart and crocheted flowers in green, orange and lilac with buttons"></div>
    <div class="brand">
      <span class="brand__mark"></span>
      <h1 class="brand__name">Tufted<br>Hollow</h1>
    </div>
    <div class="contact">
      <p class="contact__name">Dana Whitcombe</p>
      <p class="contact__phone">(555)014-2298</p>
    </div>
    <p class="contact__email">tuftedhollowbydana@example.com</p>
    <div class="services">
      <p>Hand Knit &amp; Crochet:</p>
      <p>Baby Afghans</p>
      <p>Afghans</p>
      <p>Scarves</p>
    </div>
    <div class="decor decor--cable-corner" role="img" aria-label="Pink crocheted flower over a cream cable-knit braid"></div>
  </section>
</body>
</html>
```